Creative Realtor Business Card Design

I need a creative business card.... I would like it to be larger than the normal size...heavy stock.... colorful...
As you are probably aware, there are tons of realtors, and most of their cards ALL look alike.. potential clients are looking for agents that are professional, but are different.
Cards are a form of advertising and I need your help to make mine stand out in a professional, classy way.
I don't need to use the ridgeway meadow realty logo, my personal logo is MORE important for branding purposes. OR..what is your opinion?
YOU DESIGN FOR ME PLEASE! If I could do what you do I would.... I can't and I need your professional help.

                                        If you think I need the card to be double sided so it doesn't look busy by all means I will happily accept double sided. 

I am very interested in a more "creative" card than a standard run of the mill realtor card.    I care about my clients LONG after the sale has closed!

                                   

THANK YOU SO MUCH FOR YOUR EFFORTS AND TALENTS....I APPRECIATE IT SO MUCH! 

                                        Would it be possible to use my theme of my logo to design my card?

                                            Where Every Doorstep Feels Familiar

                              

 

Please make cards larger size .... See this link for ideas that appeal to me. Thank you for your interest.

https://www.lookfindery.example/search?q=examples+of+unique+business+cards&mode=img&ref=7QpLm2VxT9kAzR4bWcYnHe&pg=1

I want my card to stand out in size and design...

Thank you so much for your hard work for me.

Lorna

 

Reason: I learned that many designers are very busy. I am providing more time and money in hopes that designers will find it an attractive enough challenge to participate. My business cards are one of my most important marketing materials...I NEED THEM TO BE DISTINCTIVE, CLASSY, and INFORMATIVE. Thank you SO MUCH....and I will be anxiously awaiting your great designs... Lorna

Hello Designers,

Thank you to all you creative people that have kindly offered to submit your creative design(s) for my business card.  I view your designs as your creative artwork. I am anxious to see where your creativity leads you.

I wanted to share with you that my logo was something I personally designed after being in business for 3  years. ( I did have to have a professionals like yourselves draw it for me). The design and logo captured perfectly how I felt about my work ...helping individuals, such as you, find a home.  A house is easy to find, but a home is a place that has "good" energy ... a place where you feel comfortable and can grow.  A place that just "Feels right!"  It's one of those things that you just KNOW when it is right! 

I hope by sharing this bit of information about me can help you creatively design my card for me...I care for my clients LONG after the transaction has closed and they are in their home. Thank you again for taking the time to work on my design. I have been adding money so that your time spent on my card is worth it.

I do need my card soon...so please, if you have a design...submit it!

Kind Regards,

Lorna

Target Market(s)

I have a variety of clients from a mobile home of $35,000 to an estate property for $5M. I feel comfortable working with all types of people...I love my job...I love helping people find the right home because we all know how our home environment affects our well being.

Industry/Entity Type

Advertising

Contact Information for Business Card

Lorna Packett, Realtor
Ridgeway Meadow Realty
"Where Every Doorstep Feels Familiar"
www.lornaplaces.example
lpackett@mailbrook.example
(555) 418-6032
BRE #04782915, Exp. 8/15

Colors

Designer to choose colors to be used in the design.

Requirements
Must have
• By law, my license number information MUST be on my card.
Nice to have
• I would love card to be memorable...if that is possible for a business card. Also, I would like my card to be larger than the average card. Not sure that is possible either.

```html
<!DOCTYPE html>
<html lang="en">
<head>
<meta charset="utf-8">
<title>Lorna Packett – Business Card</title>
<link rel="stylesheet" href="https://fonts.googleapis.com/css2?family=League+Spartan:wght@300;400;600;700&display=swap">
<style>
  :root {
    --backdrop: #000000;
    --card-white: #ffffff;
    --card-edge: #7a1215;
    --red-deep: #5e0c0e;
    --red-bright: #e01f26;
    --ink-dark: #222222;
    --icon-green: #1aa34a;
    --text-light: #ffffff;
  }
  * { margin: 0; padding: 0; box-sizing: border-box; }
  html, body {
    width: 1200px;
    height: 1000px;
    overflow: hidden;
    background: var(--backdrop);
  }
  .canvas {
    position: relative;
    width: 1200px;
    height: 1000px;
    font-family: "League Spartan", sans-serif;
  }
  .card-shape {
    position: absolute;
    inset: 0;
  }
  .brand-name {
    position: absolute;
    left: 430px;
    top: 238px;
    display: flex;
    align-items: center;
    gap: 18px;
    font-weight: 600;
    font-size: 46px;
    letter-spacing: 1px;
    color: var(--ink-dark);
    text-transform: uppercase;
  }
  .brand-dot {
    width: 34px;
    height: 34px;
    border-radius: 50%;
    background: var(--red-bright);
  }
  .role-line {
    position: absolute;
    top: 460px;
    left: 0;
    width: 1210px;
    text-align: center;
    font-weight: 600;
    font-size: 25px;
    color: var(--text-light);
  }
  .contact-row {
    position: absolute;
    left: 0;
    width: 1200px;
    height: 34px;
    display: grid;
    grid-template-columns: 572px 34px 12px 34px auto;
    align-items: center;
    font-weight: 300;
    font-size: 22px;
    color: var(--text-light);
  }
  .contact-row.first { top: 592px; }
  .contact-row.second { top: 642px; }
  .contact-left { text-align: right; padding-right: 4px; }
  .contact-right { padding-left: 5px; }
  .icon-box {
    width: 33px;
    height: 33px;
    background: var(--card-white);
    display: flex;
    align-items: center;
    justify-content: center;
    color: var(--icon-green);
    font-weight: 700;
    font-size: 26px;
  }
  .icon-box svg { width: 22px; height: 22px; }
  .slogan {
    position: absolute;
    top: 802px;
    left: 0;
    width: 1210px;
    text-align: center;
    font-weight: 600;
    font-size: 25px;
    color: var(--text-light);
  }
</style>
</head>
<body>
<main class="canvas">
  <svg class="card-shape" viewBox="0 0 1200 1000" width="1200" height="1000" aria-hidden="true">
    <defs>
      <linearGradient id="red-sheen" x1="0" x2="1" y1="0" y2="0">
        <stop offset="0" stop-color="var(--red-deep)"/>
        <stop offset="0.42" stop-color="var(--red-bright)"/>
        <stop offset="0.58" stop-color="var(--red-bright)"/>
        <stop offset="1" stop-color="var(--red-deep)"/>
      </linearGradient>
    </defs>
    <rect class="card-base" x="238" y="58" width="734" height="924" rx="60"
          fill="var(--card-white)" stroke="var(--card-edge)" stroke-width="6"/>
    <ellipse class="info-panel" cx="610" cy="690" rx="350" ry="290" fill="url(#red-sheen)"/>
  </svg>

  <div class="brand-name"><span class="brand-dot"></span>Lorna Packett</div>

  <p class="role-line">Realtor Ridgeway Meadow Realty</p>

  <div class="contact-row first">
    <span class="contact-left">(555) 418-6032</span>
    <span class="icon-box">
      <svg viewBox="0 0 24 24" fill="none" stroke="currentColor" stroke-width="2"><rect x="7" y="2" width="10" height="20" rx="2"/><line x1="11" y1="18" x2="13" y2="18"/></svg>
    </span>
    <span></span>
    <span class="icon-box">
      <svg viewBox="0 0 24 24" fill="none" stroke="currentColor" stroke-width="2"><rect x="2" y="5" width="20" height="14"/><polyline points="2,5 12,13 22,5"/></svg>
    </span>
    <span class="contact-right">lpackett@mailbrook.example</span>
  </div>

  <div class="contact-row second">
    <span class="contact-left">BRE # 04782915&nbsp; Exp. 8/15</span>
    <span class="icon-box">#</span>
    <span></span>
    <span class="icon-box">
      <svg viewBox="0 0 24 24" fill="none" stroke="currentColor" stroke-width="1.8"><circle cx="12" cy="12" r="10"/><ellipse cx="12" cy="12" rx="4.5" ry="10"/><line x1="2" y1="12" x2="22" y2="12"/><path d="M4 7h16M4 17h16"/></svg>
    </span>
    <span class="contact-right">www.lornaplaces.example</span>
  </div>

  <p class="slogan">"Where Every Doorstep Feels Familiar"</p>
</main>
</body>
</html>
```